Kestrel Wiring - Electrician company flyers for new clients

I want a flyer that will be dropped into mailboxes and will hopefully stand out more that the ones i have tried to mock up. I have attached my latest design to give you an idea but it is rather boring.

The aim is obviously to entice new customers into calling me for any electrical work, mainly domestic but i also do commercial work.
I will also upload a photo of my business card so that it can be used as a reference and my website is www.kestrelwiring.co.nz for any extra information.

Ideally the flyer will be DL size
measurements from printmorrow is that's any help
Document Trim Size
99 x 210 mm
1169 x 2480 pixels
Full Bleed Size
102 x 213 mm
1205 x 2516 pixels

Target Market(s)

Domestic electrical works

Industry/Entity Type

Electrician

Requirements
Must have
• all of my contact details -
• Dean Forsyth
• Dean@kestrelwiring.co.nz
• 027 3815 942
• www.kestrelwiring.co.nz
• A little write up similar to the one written on my draft but there's probably alot of room for improvement as my writing skills are lacking.
Nice to have
• clear and concise writing so that people wont throw it away before reading

```html
<!DOCTYPE html>
<html lang="en">
<head>
<meta charset="utf-8">
<title>Kestrel Wiring – DL Flyer</title>
<link href="https://fonts.googleapis.com/css2?family=Arimo:wght@400;700&family=Oswald:wght@600&family=Roboto:wght@300;400;900&display=swap" rel="stylesheet">
<style>
  :root{
    --backdrop:#bde0f7;
    --paper:#ffffff;
    --blue:#0ea5e6;
    --blue-deep:#0a6ea6;
    --charcoal:#3a3a3a;
    --grey:#5b5b5b;
    --grey-soft:#7a7a7a;
  }
  *{box-sizing:border-box;margin:0;padding:0}
  html,body{width:1200px;height:1200px;overflow:hidden;background:var(--backdrop)}
  body{position:relative;font-family:"Arimo",Arial,sans-serif;color:var(--grey)}

  .flyer{position:absolute;top:183px;width:403px;height:854px;background:var(--paper);overflow:hidden}
  .flyer--front{left:146px}
  .flyer--back{left:653px}
  .flyer > *{position:absolute}

  .brand{left:0;right:0;top:44px;text-align:center;font-family:"Arimo",Arial,sans-serif;font-weight:700;font-size:25px;letter-spacing:1px;color:var(--charcoal);text-transform:uppercase}
  .flyer--front .brand{right:45px}

  /* front */
  .side-band{right:0;top:0;width:45px;height:452px;background:linear-gradient(var(--blue),var(--blue-deep));border-bottom-left-radius:45px}
  .hero{left:0;top:116px;width:391px;height:293px}
  .headline-top{left:0;right:0;top:458px;text-align:center;font-weight:700;font-size:27px;color:var(--charcoal);letter-spacing:.5px}
  .headline-main{left:0;right:0;top:490px;text-align:center;font-weight:700;font-size:40px;color:var(--blue);letter-spacing:.5px}
  .tagline{left:40px;top:544px;width:316px;height:45px;border:1.5px solid var(--grey);text-align:center;font-family:"Roboto",Arial,sans-serif;font-weight:300;font-size:16px;line-height:20px;padding-top:2px;color:var(--grey)}
  .foot-band{left:0;top:602px;width:42px;height:252px;background:linear-gradient(var(--blue),var(--blue-deep));border-top-right-radius:42px}
  .feature{left:23px;width:360px;display:flex;align-items:flex-start}
  .feature__icon{width:34px;height:34px;border-radius:50%;background:var(--charcoal);border:2.5px solid #fff;box-shadow:0 0 0 1px #ccc;flex:none;display:flex;align-items:center;justify-content:center}
  .feature__label{width:78px;margin-left:9px;margin-top:3px;font-size:8.6px;line-height:10.5px;color:var(--charcoal);text-transform:uppercase}
  .feature__label span{color:var(--blue);display:block}
  .feature__text{width:229px;margin-left:0;font-size:6.6px;line-height:8.6px;color:var(--grey-soft);text-align:justify}
  .feature--1{top:643px}
  .feature--2{top:706px}
  .feature--3{top:766px}
  .web-tab{right:0;top:812px;width:192px;height:42px;background:var(--charcoal);border-top-left-radius:30px;color:#fff;font-size:10px;letter-spacing:.6px;padding:16px 0 0 35px}

  /* back */
  .question{left:0;right:0;top:112px;text-align:center;font-family:"Roboto",Arial,sans-serif;font-weight:300;font-size:19.5px;line-height:25px;color:var(--grey)}
  .question span{color:var(--blue);display:block}
  .rule{left:162px;top:168px;width:79px;height:2px;background:var(--blue)}
  .intro{left:30px;width:343px;text-align:center;font-family:"Roboto",Arial,sans-serif;font-weight:300;font-size:9.6px;line-height:12.2px;color:var(--grey)}
  .intro--1{top:182px}
  .intro--2{top:242px}
  .showcase{left:0;top:309px;width:403px;height:294px}
  .contact{left:48px;top:657px;width:308px;height:52px;border:2px solid var(--charcoal);border-radius:16px;text-align:center}
  .contact__name{position:absolute;left:0;right:0;top:19px;font-family:"Roboto",Arial,sans-serif;font-weight:900;font-size:18.5px;letter-spacing:.6px;color:var(--charcoal);text-transform:uppercase}
  .contact__pill{left:121px;top:643px;width:160px;height:30px;border-radius:15px;background:linear-gradient(var(--blue),var(--blue-deep));border:3px solid #fff;box-sizing:content-box;margin:-3px;color:#fff;font-family:"Oswald",Arial,sans-serif;font-weight:600;font-size:16px;line-height:30px;text-align:center;letter-spacing:.3px}
  .contact-line{left:0;right:0;text-align:center;font-size:10px;letter-spacing:.3px;color:var(--grey)}
  .contact-line__icon{display:block;margin:0 auto 5px;width:22px;height:22px;border-radius:50%;background:var(--blue);display:flex;align-items:center;justify-content:center}
  .contact-line--mail{top:729px}
  .contact-line--web{top:774px}
  .back-footer{left:0;top:833px;width:403px;height:21px}
</style>
</head>
<body>

<section class="flyer flyer--front">
  <div class="side-band"></div>
  <div class="brand">Kestrel Wiring</div>

  <svg class="hero" viewBox="0 0 391 293" role="img" aria-label="Photo: electrician in hard hat holding two sparking cables above a night city">
    <defs>
      <radialGradient id="heroGlow" cx="0.55" cy="0.25" r="0.8">
        <stop offset="0" stop-color="#cfe9ff"/>
        <stop offset="0.25" stop-color="#3f7fd0"/>
        <stop offset="0.7" stop-color="#163a78"/>
        <stop offset="1" stop-color="#0c1f45"/>
      </radialGradient>
    </defs>
    <path d="M0 0 H360 A31 31 0 0 1 391 31 V262 A31 31 0 0 1 360 293 H0 Z" fill="url(#heroGlow)"/>
    <polygon points="0,0 100,0 12,163 64,163 0,286" fill="#4a4a4a"/>
    <polyline points="106,0 17,165 69,165 4,293" fill="none" stroke="#fff" stroke-width="8" stroke-linejoin="miter"/>
  </svg>

  <h1 class="headline-top">RELIABLE AND</h1>
  <h2 class="headline-main">PROFESSIONAL</h2>
  <p class="tagline">BRING OUR UNPARALLELED SERVICE<br>TO YOUR PROJECT!</p>

  <div class="foot-band"></div>

  <div class="feature feature--1">
    <div class="feature__icon">
      <svg width="16" height="16" viewBox="0 0 16 16"><path d="M8 1 L14 3.5 V8 C14 11.5 11 14 8 15 C5 14 2 11.5 2 8 V3.5 Z" fill="none" stroke="#fff" stroke-width="1.5"/><path d="M5 8 L7.2 10.2 L11 6" fill="none" stroke="#fff" stroke-width="1.5"/></svg>
    </div>
    <p class="feature__label"><span>Reliable</span>Electricians</p>
    <p class="feature__text">Specializing in residential and commercial electrical services, we are dedicated to providing customer service that is second to none. Whether you need a small wiring fix or the full installation, we can get the job done right.</p>
  </div>

  <div class="feature feature--2">
    <div class="feature__icon">
      <svg width="16" height="16" viewBox="0 0 16 16"><circle cx="8" cy="8" r="5" fill="none" stroke="#fff" stroke-width="2.6" stroke-dasharray="2.2 1.4"/><path d="M5.5 8 L7.3 9.8 L10.8 6.3" fill="none" stroke="#fff" stroke-width="1.5"/></svg>
    </div>
    <p class="feature__label"><span>Flexible</span>Services</p>
    <p class="feature__text">We provide you with a full consultation to explain your available options so that you can choose the scope of work that's right for your home or business - and your budget.</p>
  </div>

  <div class="feature feature--3">
    <div class="feature__icon">
      <svg width="16" height="16" viewBox="0 0 16 16"><rect x="2" y="2" width="12" height="4" rx="1" fill="none" stroke="#fff" stroke-width="1.1"/><circle cx="8" cy="9.5" r="1.8" fill="#fff"/><path d="M4.5 15 C4.5 12 11.5 12 11.5 15 Z" fill="#fff"/></svg>
    </div>
    <p class="feature__label"><span>Customer<br>Satisfaction</span>Guaranteed</p>
    <p class="feature__text">We strive to save you both time and money by combining our deep experience, the highest quality parts and equipment, and our dedication to delivering exceptional service. We will not leave the job until you are satisfied.</p>
  </div>

  <div class="web-tab">www.kestrelwiring.co.nz</div>
</section>

<section class="flyer flyer--back">
  <div class="brand">Kestrel Wiring</div>

  <h2 class="question"><span>DO YOU NEED A LOCAL AND</span>RELIABLE ELECTRICIAN?</h2>
  <div class="rule"></div>

  <p class="intro intro--1">Specializing in residential and commercial electrical services, we are dedicated to providing customer service that is second to none. Whether you need a small wiring fix or the full installation, we can get the job done right.</p>
  <p class="intro intro--2">Based in Kowhai Bay, we are your local electricians with our main aim to keep our work and communication to a very high standard.</p>

  <svg class="showcase" viewBox="0 0 403 294" role="img" aria-label="Photo: electrician holding a coil of cable beside tools and wiring plans">
    <defs>
      <linearGradient id="plans" x1="0" x2="1">
        <stop offset="0" stop-color="#ececec"/>
        <stop offset="1" stop-color="#d7d7d7"/>
      </linearGradient>
      <linearGradient id="panel" x1="0" y1="0" x2="0" y2="1">
        <stop offset="0" stop-color="#0ea5e6"/>
        <stop offset="1" stop-color="#0b86c4"/>
      </linearGradient>
    </defs>
    <rect width="403" height="294" fill="url(#plans)"/>
    <polygon points="246,0 403,0 403,294 143,294" fill="url(#panel)"/>
    <polygon points="236,0 246,0 143,294 133,294" fill="#4a4a4a"/>
    <polygon points="250,50 190,175 210,175 150,294 157,294 225,168 204,168 258,50" fill="#ffffff"/>
  </svg>

  <div class="contact">
    <p class="contact__name">Dean Forsyth 027 3815 942</p>
  </div>
  <div class="contact__pill">CONTACT US TODAY</div>

  <div class="contact-line contact-line--mail">
    <span class="contact-line__icon">
      <svg width="11" height="8" viewBox="0 0 11 8"><rect x="0.5" y="0.5" width="10" height="7" fill="#fff"/><path d="M0.5 0.5 L5.5 4.5 L10.5 0.5" fill="none" stroke="#0ea5e6" stroke-width="1"/></svg>
    </span>
    dean@kestrelwiring.co.nz
  </div>
  <div class="contact-line contact-line--web">
    <span class="contact-line__icon">
      <svg width="12" height="12" viewBox="0 0 12 12"><circle cx="6" cy="6" r="5" fill="none" stroke="#fff" stroke-width="1.2"/><ellipse cx="6" cy="6" rx="2.2" ry="5" fill="none" stroke="#fff" stroke-width="1"/><line x1="1" y1="6" x2="11" y2="6" stroke="#fff" stroke-width="1"/></svg>
    </span>
    www.kestrelwiring.co.nz
  </div>

  <svg class="back-footer" viewBox="0 0 403 21" aria-hidden="true">
    <rect x="0" y="12" width="224" height="9" fill="#0ea5e6"/>
    <path d="M221 21 C228 8 236 0 252 0 H403 V21 Z" fill="#3a3a3a"/>
  </svg>
</section>

</body>
</html>
```